Dufresne Roofing

Want a professional looking business card

Industry/Entity Type

Business

Contact Information for Business Card

Marc Dufresne ( Owner) marc@dufresneroofing-example.com, www.dufresneroofing-example.com, Adress: 4217 County road 42 Wendover,ON K0A3M1

```html
<!DOCTYPE html>
<html lang="en">
<head>
<meta charset="utf-8">
<title>Dufresne Roofing — Business Card</title>
<link rel="stylesheet" href="https://fonts.googleapis.com/css2?family=Open+Sans:wght@400;600;700&display=swap">
<style>
  :root {
    --stage: #000000;
    --card-light: #f0f0f0;
    --brand-blue: #1d4784;
    --ink-blue: #1c3f7a;
    --ink-grey: #3a3a3a;
    --silver: #d9d9d9;
    --rule: #2a4c86;
  }
  * { margin: 0; padding: 0; box-sizing: border-box; }
  html, body {
    width: 1200px; height: 900px; overflow: hidden;
    background: var(--stage);
    font-family: "Open Sans", Arial, sans-serif;
  }
  .canvas { position: relative; width: 1200px; height: 900px; }

  .card { position: absolute; top: 275px; width: 477px; height: 294px; }
  .card-front {
    left: 116px; background: var(--card-light);
    border-radius: 0 46px 0 46px;
  }
  .card-back {
    left: 622px; background: var(--brand-blue);
    border-radius: 46px 0 46px 0;
  }

  .wordmark {
    position: absolute; right: 28px; top: 44px;
    display: flex; align-items: center; gap: 10px;
    color: var(--brand-blue); font-weight: 700;
    font-size: 27px; letter-spacing: 1px; line-height: 1.1;
    text-align: right;
  }
  .wordmark .dot {
    width: 14px; height: 14px; background: var(--brand-blue);
  }
  .wordmark span.name { display: block; width: 200px; }

  .holder { position: absolute; left: 27px; top: 172px; }
  .holder-name {
    color: var(--ink-blue); font-weight: 700; font-size: 19px;
    letter-spacing: 0.2px; line-height: 1.1;
  }
  .holder-role { color: var(--ink-grey); font-size: 13px; margin-top: 4px; }
  .name-rule {
    position: absolute; left: 194px; right: 27px; top: 184px;
    height: 1.5px; background: var(--rule);
  }

  .address {
    position: absolute; left: 27px; top: 230px;
    color: var(--ink-grey); font-size: 13px; line-height: 18px;
  }
  .contact {
    position: absolute; right: 26px; top: 230px;
    color: var(--ink-grey); font-size: 13px; line-height: 18px;
    list-style: none; text-align: right;
  }
  .contact li { display: flex; align-items: center; justify-content: flex-end; gap: 6px; }
  .contact svg { width: 11px; height: 11px; flex: none; }

  .back-wordmark {
    position: absolute; inset: 0;
    display: flex; align-items: center; justify-content: center;
    color: var(--silver); font-weight: 700; font-size: 34px;
    letter-spacing: 1.5px; text-align: center; line-height: 1.15;
  }
</style>
</head>
<body>
<main class="canvas">
  <section class="card card-front" aria-label="Business card front">
    <div class="wordmark">
      <span class="name">DUFRESNE ROOFING</span>
      <span class="dot" aria-hidden="true"></span>
    </div>

    <div class="holder">
      <p class="holder-name">MARC DUFRESNE</p>
      <p class="holder-role">Owner</p>
    </div>
    <div class="name-rule" aria-hidden="true"></div>

    <address class="address" style="font-style:normal">
      4217 County road 42<br>
      Wendover,ON K0A3M1
    </address>

    <ul class="contact">
      <li>marc@dufresneroofing-example.com
        <svg viewBox="0 0 12 12" aria-hidden="true">
          <rect x="0.5" y="2" width="11" height="8" fill="var(--brand-blue)"/>
          <path d="M0.8 2.4 L6 6.6 L11.2 2.4" fill="none" stroke="#ffffff" stroke-width="1"/>
        </svg>
      </li>
      <li>www.dufresneroofing-example.com
        <svg viewBox="0 0 12 12" aria-hidden="true">
          <circle cx="6" cy="6" r="5.5" fill="var(--brand-blue)"/>
          <ellipse cx="6" cy="6" rx="2.3" ry="5" fill="none" stroke="#ffffff" stroke-width="0.8"/>
          <line x1="1" y1="6" x2="11" y2="6" stroke="#ffffff" stroke-width="0.8"/>
        </svg>
      </li>
    </ul>
  </section>

  <section class="card card-back" aria-label="Business card back">
    <div class="back-wordmark">DUFRESNE<br>ROOFING</div>
  </section>
</main>
</body>
</html>
```